WordPress Template
Ravenfield Staffing, Inc.
Thank you all for you designs! A lot of great ideas, and I appreciate your effort.
Re: 94, thank you, but the image doesn't really work for me.
Re: 71 and similar -- very nice! I'm going to get feedback from others on my team about those and the others I haven't eliminated. Thank you!
Re: 61 and similar, thank you, but that image doesn't work for me.
Re: 57, can I see that with the oval steps you did in 44? Thanks!
Re: 75-78, thank you, but I don't like the image with the people.
thanks,
BrightquillStudio
On 55 and 56, I think I prefer the image to be next to the words, as in 44. Making the star red is nice little touch, and I do like the smaller stars rather than the larger as in 44. Thanks!
On 46, thank you. Overall, I like the look and feel of it. I'm thinking about the upper right corner image...maybe a slightly smaller star? I"m not sure if I'm going to be on all the social media or not, so the bottom left will need something there if not.
On 51, I like the ladder since it plays off the idea of climbing the ladder of success, but would it be possible to do a ladder that's a bit less real looking? Thanks!
Re: 47-54, thank you! I've eliminated the ones where the images don't work for me for whatever reason. I like the overall layout and design, but would like to see a bit more red and/or other contrast to punch it up a bit. Thanks so much!
***The font in the logo is Geosans Light, and I'd like no more than 2 fonts total in the design (so Geosans Light plus one other).*** Thank you!
On 25, can you play with the colors a bit and get rid of the Shape Your Morning on the far right top? Also I'm not keen on the look of that menu bar. Thanks!
On 40, can you add in a figure on the stairs or maybe just the figure using the star/endless possibilities concept on the bottom right or in the middle right someplace? And omit the second logo on the far left in the middle. And instead of the Shape Your Morning restated in the middle next to the second logo image, let's use The Possibilities are Endless, You Just Have to Know Where to Look. Thank you!
Re: 38, thank you, the figure on the stairs is moving in the right direction, I think. What about eliminating the building part? And/or maybe moving the figure/stairs to the bottom by the text? Thanks!
Thank you for 33-37. Please note my prior comments on not wanting to include the Shape Your Morning on the top right from the old design. Overall, I'm not sure any of these really grab me...although I do want simple, these are all very plain looking. Thank you for submitting, though.
Hi PH,
please feel free to let me know the required changes so that your expectations are met.
Awaiting for your kind feedback
Polaris
Thank you for 26-31. None of those are really working....I think having the image on both top and bottom looks too busy, and please omit the old "shape your morning" on the top right. I think using some version of the figure in the D is probably the way to go, but the overall look of 25 doesn't really work. Thank you!
What about something that uses the little figure from the D on the logo, combined with some sort of concept of limitlessness? This instead of the figure from the old site....
Hi,
I think the old graphic shouldn't be a prob as that seems very abstract that depict growth and success.
Thank you for 22 - 24. Please, no actual images of people for reasons stated previously. Also not very keen on random clip-art looking images as used on the bottom. I really like a clean style. I see what you were doing with the stairs to the right, but with the guy climbing up them, it just looks like hard work again. The image in the old site looks whimsical and "reach for the stars" instead of the hard work of climbing stairs.
On 21, I think we also need to get rid of the Shape Your Morning on the far right (the one that's left over from the old site). Also, it does look odd without another graphic to the right of the text, but I just don't really think the old graphic works with the new logo.
Hi, No graphics means. Did you mean about the footer, the background I used?
Maybe something that has just the logo and the text without any other graphics?
Thank you for #20. I think I may have to let go of using that old figure....it just doesn't seem to work with the new vibe of the new logo, yet I'm not sure what to replace it with. But thank you for listening to my comments; this is a very good version based on what I was asking for, but I just don't know if it works.

```html
<!DOCTYPE html>
<html lang="en">
<head>
<meta charset="utf-8">
<title>Ravenfield Staffing, Inc.</title>
<link rel="stylesheet" href="https://fonts.googleapis.com/css2?family=Didact+Gothic&family=Arimo:wght@400;700&display=swap">
<style>
  :root {
    --red: #c4161c;
    --red-dark: #8e0c10;
    --red-light: #d9262b;
    --ink: #444444;
    --ink-soft: #666666;
    --page: #e9e9e9;
    --panel: #ffffff;
    --line: #d4d4d4;
    --grey-deep: #9a9a9a;
  }
  * { box-sizing: border-box; margin: 0; padding: 0; }
  html, body { width: 1200px; height: 715px; overflow: hidden; }
  body {
    position: relative;
    background: linear-gradient(to bottom, #f4f4f4 0%, var(--page) 60%, #e2e2e2 100%);
    font-family: "Arimo", Arial, sans-serif;
    color: var(--ink);
  }

  /* Brand */
  .brand { position: absolute; left: 168px; top: 18px; display: flex; align-items: center; gap: 14px; }
  .brand-dot { width: 64px; height: 64px; border-radius: 50%; background: var(--red); flex: none; }
  .brand-name { font-family: "Didact Gothic", sans-serif; font-size: 36px; color: var(--red-dark); letter-spacing: 0.5px; line-height: 1; }
  .brand-tagline { font-family: "Didact Gothic", sans-serif; font-size: 15px; letter-spacing: 6px; color: var(--ink); text-transform: uppercase; margin-top: 10px; }

  /* Navigation */
  .main-nav {
    position: absolute; left: 144px; top: 120px; width: 912px; height: 52px;
    background: linear-gradient(to bottom, var(--red-light) 0%, var(--red) 50%, var(--red-dark) 100%);
    border-radius: 6px 6px 0 0;
    display: flex; align-items: center; padding-left: 17px;
  }
  .main-nav a {
    font-family: "Arimo", sans-serif; font-size: 14px; text-transform: uppercase; color: #fff;
    text-decoration: none; letter-spacing: 0.4px; text-align: center;
  }
  .main-nav .nav-home {
    width: 72px; height: 34px; line-height: 34px; background: linear-gradient(#ffffff, #e4e4e4);
    color: var(--ink); border-radius: 4px; font-weight: 700; margin-right: 44px;
  }
  .main-nav .nav-item { margin-right: 64px; }

  /* Hero */
  .hero {
    position: absolute; left: 144px; top: 172px; width: 912px; height: 222px;
    background: linear-gradient(to bottom, #ffffff 0%, #fbfbfb 55%, #d9d9d9 100%);
    border-left: 1px solid var(--line); border-right: 1px solid var(--line);
  }
  .hero-text { position: absolute; left: 42px; top: 56px; width: 560px; font-family: "Arimo", sans-serif; font-size: 29px; line-height: 42px; color: var(--red); }
  .hero-art {
    position: absolute; right: 24px; top: 12px; width: 240px; height: 200px;
    background: radial-gradient(ellipse at 60% 30%, #f6e8e8 0%, #ececec 45%, #d0d0d0 100%);
    border-radius: 4px;
  }
  .hero-shadow { position: absolute; left: 144px; top: 394px; width: 912px; height: 14px; background: radial-gradient(ellipse at center top, rgba(0,0,0,0.18), transparent 70%); }

  /* Content */
  .content {
    position: absolute; left: 144px; top: 412px; width: 912px; height: 218px;
    background: var(--panel); border: 1px solid var(--line);
  }
  .intro { position: absolute; left: 22px; top: 14px; width: 600px; }
  .section-title { font-family: "Didact Gothic", sans-serif; font-size: 25px; color: var(--red-dark); padding-bottom: 6px; border-bottom: 1px solid var(--line); }
  .intro p { font-size: 12px; line-height: 19px; color: var(--ink-soft); margin-top: 14px; }
  .intro .intro-lead { font-size: 15px; line-height: 22px; color: var(--red); margin-top: 16px; }
  .divider { position: absolute; left: 646px; top: 0; width: 1px; height: 216px; background: var(--line); }

  .testimonials { position: absolute; left: 672px; top: 14px; width: 218px; }
  .testimonials .section-title { border-bottom: none; padding-bottom: 0; }
  .quote-box {
    margin-top: 16px; padding: 10px 10px; background: linear-gradient(#ffffff, #f2f2f2);
    border: 1px solid #e6e6e6; font-family: Georgia, serif; font-size: 11px; line-height: 15px; color: var(--ink);
  }
  .quote-author { text-align: right; font-family: Georgia, serif; font-weight: 700; font-size: 11px; margin-top: 8px; color: var(--ink); }
  .read-more {
    position: absolute; right: 0; top: 180px; padding: 3px 10px; font-size: 12px; font-weight: 700; color: var(--red);
    background: #f1f1f1; border-radius: 3px; text-decoration: none;
  }

  /* Footer */
  .footer-nav { position: absolute; left: 0; top: 640px; width: 1200px; text-align: center; font-size: 12px; color: var(--ink); }
  .footer-nav a { color: var(--ink); text-decoration: none; padding: 0 7px; }
  .footer-nav a.current { color: var(--red); }
  .footer-nav .sep { color: var(--ink); }
  .footer-rule { position: absolute; left: 144px; top: 674px; width: 912px; height: 1px; background: var(--grey-deep); }
  .copyright { position: absolute; left: 144px; top: 688px; font-size: 10px; color: var(--grey-deep); }
</style>
</head>
<body>
  <header class="brand">
    <span class="brand-dot"></span>
    <div>
      <div class="brand-name">Ravenfield Staffing, Inc.</div>
      <div class="brand-tagline">Shape your morning</div>
    </div>
  </header>

  <nav class="main-nav">
    <a class="nav-home" href="#">Home</a>
    <a class="nav-item" href="#">Your Team</a>
    <a class="nav-item" href="#">Our Mission</a>
    <a class="nav-item" href="#">Attorneys</a>
    <a class="nav-item" href="#">Law Firms</a>
    <a class="nav-item" href="#">Contact Us</a>
  </nav>

  <section class="hero">
    <p class="hero-text">The possibilities are endless<br>You just need to know where to look.</p>
    <div class="hero-art" role="img" aria-label="Illustration of a small figure reaching for a red star above rising round stepping stones among sparkles"></div>
  </section>
  <div class="hero-shadow"></div>

  <main class="content">
    <article class="intro">
      <h2 class="section-title">Shape Your Morning</h2>
      <p>The possibilities are endless. You just need to know where to look.</p>
      <p>And that's what we're here for. We can help you find a new position within your current profession, or we<br>can provide advice to help to discover your true path to happiness.</p>
      <p class="intro-lead">We're here for you. We want a good match for both our candidates and our clients:<br>It's YOUR career. . . and YOUR law firm.</p>
    </article>
    <div class="divider"></div>
    <aside class="testimonials">
      <h2 class="section-title">Testimonials</h2>
      <blockquote class="quote-box">"Lorem ipsum dolor sit amet, consectetur adipiscing elit. Quisque urna mi, elementum non vulputate sed, hendrerit quis enim. Aenean sed nulla id nibh laoreet mattis at in elit."</blockquote>
      <div class="quote-author">Corbin Hale, Self</div>
      <a class="read-more" href="#">Read more »</a>
    </aside>
  </main>

  <nav class="footer-nav">
    <a class="current" href="#">Home</a><span class="sep">|</span><a href="#">Your Team</a><span class="sep">|</span><a href="#">Our Mission</a><span class="sep">|</span><a href="#">Attorneys</a><span class="sep">|</span><a href="#">Law Firms</a><span class="sep">|</span><a href="#">Contact</a>
  </nav>
  <div class="footer-rule"></div>
  <p class="copyright">Copyright © 2013 Ravenfield Staffing</p>
</body>
</html>
```